Vorn Solutions: searching for a flyer to trow in letterboxes for properties we are interested in

Hello ,

Introduction:
We are a company based in Luxembourg called "Vorn Solutions". We are specialized in buying properties on which we develop and build constructions before selling them.

Informations for the flyer:
We need a flyer to trow into the letter boxes of property owners letting them know that we are interested in buying their property, if they are interested they can give us a call.

The text for the flyer/letter is in the attachment called >>2020-03-11_VS_Text for flyer,letter there might be slight changes<<.

We need to look competent, professional and financially stable.

The flyer needs to be short and not over welling with information otherwise it will land in the trash.

We have decided that we don't want real pictures on the flyer, but shapes of any kind, blue prints, drawings are fine.

Format should be in DIN A4. We plan to print the flyer on both sides in two different languages, in other words the design will be the same on both sides only the text will be in a different language.

I also added our current logo and here is the design of the website that is under construction at the moment http://www.vornsolutions.example/. The logo's color can be changed into a different blue or uni color (all white or all black).
Updates

Hi, First time user the howl thing started faster as expected. Furthermore, I need to catch my boss to discust the project with him and he is on a lot of meetings. Please give us a little bit more time. Thanks

Target Market(s)

Property owners

Requirements
Must have
• email, phone number, tax number (RCS), Tax number , matriculation and address.
see word file in attachment for information
Nice to have
• Our company logo, in one form or an other, you can be creative, the logo is in the attachment.
Should not have
• Real pictures

```html
<!DOCTYPE html>
<html lang="fr">
<head>
<meta charset="utf-8">
<title>Vorn Solutions – Courrier propriétaires</title>
<link href="https://fonts.googleapis.com/css2?family=Poppins:wght@500;600&display=swap" rel="stylesheet">
<style>
  :root {
    --backdrop: #e9e9e9;
    --paper: #f7f7f7;
    --sky: #00b9ef;
    --brand-navy: #1a5b8c;
    --ink-light: #ffffff;
  }
  * { margin: 0; padding: 0; box-sizing: border-box; }
  html, body {
    width: 1200px; height: 1200px; overflow: hidden;
    background: var(--backdrop);
    font-family: "Poppins", sans-serif;
  }
  .flyer {
    position: absolute; left: 197px; top: 30px;
    width: 806px; height: 1140px;
    background: var(--paper);
    box-shadow: 0 10px 30px rgba(0,0,0,0.25);
    overflow: hidden;
  }
  .blueprint-texture {
    position: absolute; inset: 0;
    background: radial-gradient(ellipse at 70% 75%, rgba(255,255,255,0.10), rgba(255,255,255,0) 60%),
                linear-gradient(160deg, rgba(255,255,255,0) 30%, rgba(200,210,220,0.18) 100%);
    pointer-events: none;
  }
  .header-logo-box {
    position: absolute; left: 241px; top: 16px;
    width: 315px; height: 219px;
    background: #ffffff;
    display: flex; align-items: center; justify-content: center; gap: 12px;
  }
  .brand-square { width: 22px; height: 22px; background: var(--brand-navy); }
  .brand-name {
    font-weight: 600; font-size: 30px; color: var(--brand-navy);
    letter-spacing: 0.5px;
  }
  .letter-band {
    position: absolute; left: 0; top: 287px;
    width: 806px; height: 604px;
    background: var(--sky);
  }
  .footer-band {
    position: absolute; left: 0; top: 923px;
    width: 806px; height: 217px;
    background: var(--sky);
  }
  .letter-body {
    position: absolute; left: 42px; top: 56px; width: 714px;
    color: var(--ink-light); font-weight: 500;
    font-size: 23.5px; line-height: 29.5px;
  }
  .letter-body p { margin-bottom: 29px; }
  .letter-body .justified { text-align: justify; }
  .letter-body .signature { margin-top: 58px; }
  .footer-col {
    position: absolute; top: 74px;
    color: var(--ink-light); font-weight: 500;
    font-size: 19.5px; line-height: 24.5px;
  }
  .footer-address { left: 53px; }
  .footer-contact { left: 445px; top: 72px; }
</style>
</head>
<body>
  <div class="flyer">
    <div class="header-logo-box">
      <span class="brand-square"></span>
      <span class="brand-name">VORN SOLUTIONS</span>
    </div>

    <section class="letter-band">
      <div class="letter-body">
        <p>Madame, Monsieur,</p>
        <p class="justified">Ce courrier vous a été adressé, car votre propriété a attiré notre attention. Nous souhaiterions discuter avec vous de son éventuel rachat par notre société.</p>
        <p class="justified">En cas d’accord, nous vous assurons une décision rapide, un paiement garanti, et zéro frais d’intermédiaire.</p>
        <p>En attendant de vos nouvelles, nous restons à votre entière disposition pour tout renseignement.</p>
        <p>Salutations distinguées,</p>
        <p class="signature">L’équipe de Vorn Solutions</p>
      </div>
    </section>

    <footer class="footer-band">
      <div class="footer-col footer-address">
        Vorn Solutions sàrl<br>
        18 rue des Ateliers,<br>
        L-4012 Esch-sur-Alzette
      </div>
      <div class="footer-col footer-contact">
        Email: info@vornsolutions.example<br>
        Tel. : 621 480 375<br>
        RCS : will be added
      </div>
    </footer>

    <div class="blueprint-texture" role="img" aria-label="Faint architectural blueprint drawing in the background"></div>
  </div>
</body>
</html>
```